Business Card design - 2 sides

I need a new business card design using our new branding.
On one side of the card I need to have our logo and my contact details et. On the otherside I need to display an offer to go to our website and order a copy of our free report.
If you visit my website www.talvenmark.com.au you will see our logo and branding colours. You will also see an opt-in box with a picture of our free report and CD.
These are the details I would like on the front of the card
Logo: See attached logo file
Tag line:
Company Name: Talvenmark Partners Australia
Name: Dennis Harlow
Title: Business Developer
Address:
Level 9, 54 Quarrin Street
Sydney NSW 2000
PO Box 4862 Ellamere
NSW 2100 Australia
Telephone: 1300 486 937
Mobile: 0431 679 203
Facsimile: 1300 486 938
Email: dennis.harlow@talvenmark.com.au
Website: www.talvenmark.com.au
These are the details to go on the backside of the card
Picture of Report and CD (see attached image file)
Offer:
ATTENTION: Importers and Exporters...
REVEALED AT LAST!! The 5 Critical Qualities Your Currency Exchange Provider Must Have!
Claim your complimentary copy of “The Steady Trader's Handbook for
Well-Run Overseas Payment Deals”” (valued at $97)
Simply go to www.talvenmark.com.au
Attachments: I have attached
1. PSD file of our Free report
2. PNG file of our logo (Main logo is blue and green lettering: Logo2)
3. PNG file of alternative logo, I'm not sure if this will be needed but included anyway (white and green lettering: Logo3)
Best regards,
Dennis
Business Owners and Financial Controllers of Import/Export companies.
Business

```html
<!DOCTYPE html>
<html lang="en">
<head>
<meta charset="utf-8">
<title>Talvenmark Partners Australia – Business Card</title>
<link rel="stylesheet" href="https://fonts.googleapis.com/css2?family=Questrial&display=swap">
<style>
  :root {
    --navy: #10336e;
    --navy-deep: #0d2a5c;
    --lime: #9ac31c;
    --paper: #ffffff;
    --paper-shade: #eef0f3;
    --backdrop: #2b2b2b;
  }
  * { box-sizing: border-box; margin: 0; padding: 0; }
  html, body { width: 1200px; height: 900px; overflow: hidden; }
  body {
    background: var(--backdrop);
    font-family: "Questrial", "Century Gothic", sans-serif;
    color: var(--navy);
    position: relative;
  }
  .card {
    position: absolute;
    left: 250px;
    width: 700px;
    height: 400px;
    background: linear-gradient(160deg, var(--paper) 55%, var(--paper-shade));
    overflow: hidden;
    box-shadow: 0 6px 20px rgba(0,0,0,.45);
  }
  .card--offer { top: 35px; }
  .card--contact { top: 465px; }

  .brand {
    position: absolute;
    display: flex;
    align-items: center;
    gap: 10px;
  }
  .brand__dot {
    width: 28px; height: 28px;
    border-radius: 50%;
    background: var(--lime);
  }
  .brand__name {
    font-size: 36px;
    letter-spacing: 1px;
    color: var(--navy);
    white-space: nowrap;
  }

  /* offer side */
  .card--offer .brand { left: 60px; top: 60px; }
  .offer-band {
    position: absolute;
    inset: 0;
    background: var(--navy-deep);
    clip-path: polygon(0 80%, 100% 50%, 100% 100%, 0 100%);
  }
  .offer-headline {
    position: absolute;
    left: 60px; top: 150px;
    font-size: 16px;
    line-height: 22px;
    color: var(--navy);
    white-space: nowrap;
  }
  .offer-headline strong { font-weight: 700; }
  .offer-claim {
    position: absolute;
    left: 60px; top: 328px;
    font-size: 14px;
    line-height: 20px;
    color: var(--paper);
    white-space: nowrap;
  }
  .offer-claim strong { font-weight: 700; }
  .report-visual {
    position: absolute;
    right: 40px; top: 95px;
    width: 150px; height: 110px;
    background: linear-gradient(135deg, #f4f6f8, #c9d3dc 60%, #d7e8a8);
    border-radius: 3px;
    box-shadow: 0 3px 8px rgba(0,0,0,.25);
  }

  /* contact side */
  .card--contact .brand { left: 55px; top: 70px; }
  .tagline {
    position: absolute;
    left: 318px; top: 80px;
    font-size: 18px;
    color: var(--navy);
    white-space: nowrap;
  }
  .person { position: absolute; left: 80px; top: 165px; }
  .person__name { font-size: 28px; font-weight: 400; }
  .person__title { font-size: 14px; margin-top: 2px; }
  .contact-list {
    position: absolute;
    left: 80px; top: 240px;
    list-style: none;
    font-size: 16px;
    line-height: 20px;
  }
  .contact-list li { display: flex; align-items: center; gap: 14px; white-space: nowrap; }
  .contact-list svg { width: 14px; height: 14px; fill: var(--lime); flex: none; }
  .divider {
    position: absolute;
    left: 430px; top: 215px;
    width: 2px; height: 110px;
    background: var(--lime);
  }
  .address {
    position: absolute;
    left: 448px; top: 215px;
    font-style: normal;
    font-size: 15px;
    line-height: 20px;
    white-space: nowrap;
  }
  .address strong { font-weight: 700; }
  .contact-band {
    position: absolute;
    left: 0; right: 0; bottom: 0;
    height: 40px;
    background: var(--lime);
  }
</style>
</head>
<body>

<section class="card card--offer" aria-label="Card back: free report offer">
  <div class="offer-band"></div>
  <div class="brand">
    <span class="brand__dot"></span>
    <span class="brand__name">Talvenmark</span>
  </div>
  <p class="offer-headline">
    <strong>ATTENTION:</strong> Importers and Exporters...<br>
    <strong>REVEALED AT LAST!!</strong> The 5 Critical Qualities<br>
    Your Currency Exchange Provider Must Have!
  </p>
  <div class="report-visual" role="img" aria-label="Free report booklet and CD"></div>
  <p class="offer-claim">
    Claim your complimentary copy of “The Steady Trader's Handbook for<br>
    Well-Run Overseas Payment Deals” (valued at $97)<br>
    Simply go to <strong>www.talvenmark.com.au</strong>
  </p>
</section>

<section class="card card--contact" aria-label="Card front: contact details">
  <div class="brand">
    <span class="brand__dot"></span>
    <span class="brand__name">Talvenmark</span>
  </div>
  <p class="tagline">Finally...Forex Transactions Made Easy!</p>

  <div class="person">
    <h1 class="person__name">Dennis Harlow</h1>
    <p class="person__title">Business Developer</p>
  </div>

  <ul class="contact-list">
    <li><svg viewBox="0 0 14 14" aria-hidden="true"><circle cx="7" cy="7" r="7"/><path d="M4 4h2l1 2-1 1a5 5 0 0 0 1 1l1-1 2 1v2c-4 0-6-2-6-6z" fill="#fff"/></svg>1300 486 937</li>
    <li><svg viewBox="0 0 14 14" aria-hidden="true"><rect x="3" y="0" width="8" height="14" rx="1.5"/><rect x="4.5" y="2" width="5" height="8" fill="#fff"/></svg>0431 679 203</li>
    <li><svg viewBox="0 0 14 14" aria-hidden="true"><rect x="3" y="0" width="8" height="5"/><rect x="0" y="5" width="14" height="6" rx="1"/><rect x="3" y="9" width="8" height="5"/></svg>1300 486 938</li>
    <li><svg viewBox="0 0 14 14" aria-hidden="true"><rect x="0" y="2" width="14" height="10" rx="1"/><path d="M1 3l6 5 6-5" stroke="#fff" stroke-width="1.2" fill="none"/></svg>dennis.harlow@talvenmark.com.au</li>
    <li><svg viewBox="0 0 14 14" aria-hidden="true"><circle cx="7" cy="7" r="7"/><path d="M0 7h14M7 0v14M2 3.5h10M2 10.5h10" stroke="#fff" stroke-width="0.9"/><ellipse cx="7" cy="7" rx="3" ry="7" stroke="#fff" stroke-width="0.9" fill="none"/></svg>www.talvenmark.com.au</li>
  </ul>

  <div class="divider"></div>
  <address class="address">
    <strong>Talvenmark Partners Australia</strong><br>
    Level 9, 54 Quarrin Street<br>
    Sydney NSW 2000<br>
    PO Box 4862 Ellamere<br>
    NSW 2100 Australia
  </address>

  <div class="contact-band"></div>
</section>

</body>
</html>
```